Professionelles Webdesign für hochwertiges Coaching Business
Zielgruppe
Es geht um eine Coaching-Firma für Einzelcoaching, Team-Coaching in Firmen und Ausbildungen. Inhalt sind Kommunikation, Stressmanagement und Leistungssteigerung, Persönlichkeitsentwicklung bis hin zum Marketing für Coaches.
Aufgabenstellung
- siehe Briefing im Dateiupload
- Umsetzung via Baukastensystem. Wichtig ist, dass die Features mit dem Baukastensystem umsetzbar sind.
- Es dürfen bitte diese 4 Seiten gestaltet werden:
Startseite
Coaching
Training
Ausbildung
- Obgleich ich Kundenfokus auf der Website bevorzuge, darf sie mich auch etwas widerspiegeln. Für einen Eindruck über mich sind zwei Bilder dem Anhang beigefügt. Diese Bilder sollen NICHT in die Website eingebunden werden.

```html
<!DOCTYPE html>
<html lang="de">
<head>
<meta charset="utf-8">
<title>Lindqvist – Training &amp; Coaching</title>
<link rel="stylesheet" href="https://fonts.googleapis.com/css2?family=Nunito+Sans:wght@300;400;600&display=swap">
<style>
  :root {
    --ink: #2b2f33;
    --nav: #3a3f44;
    --brand-red: #b01f2a;
    --white: #ffffff;
    --hero-overlay: rgba(20, 24, 22, 0.35);
    --help-bg: #1c1c1c;
  }
  * { margin: 0; padding: 0; box-sizing: border-box; }
  html, body {
    width: 1200px; height: 739px; overflow: hidden;
    background: var(--white);
    font-family: "Nunito Sans", Arial, sans-serif;
  }
  .page { position: relative; width: 1200px; height: 739px; }

  .site-header {
    position: absolute; inset: 0 0 auto 0; height: 122px;
    background: var(--white);
  }
  .brand {
    position: absolute; left: 54px; top: 42px;
    display: flex; align-items: center; gap: 12px;
  }
  .brand-dot { width: 34px; height: 34px; border-radius: 50%; background: var(--brand-red); }
  .brand-name {
    font-size: 27px; font-weight: 600; letter-spacing: 2px;
    color: var(--ink); text-transform: uppercase;
  }
  .main-nav {
    position: absolute; left: 355px; top: 52px;
    display: flex; gap: 21px;
  }
  .main-nav a {
    font-size: 12px; color: var(--nav); text-decoration: none; font-weight: 400;
  }
  .header-links {
    position: absolute; left: 952px; top: 52px;
    display: flex; align-items: center; gap: 20px;
  }
  .profile-link { font-size: 11px; font-weight: 600; color: var(--nav); text-decoration: none; }
  .mail-link { display: block; width: 13px; height: 10px; }
  .btn-book {
    position: absolute; left: 1039px; top: 39px; width: 111px; height: 43px;
    background: var(--brand-red); color: var(--white);
    font-size: 11px; font-weight: 600; text-decoration: none;
    display: flex; align-items: center; justify-content: center;
  }

  .hero {
    position: absolute; left: 0; top: 122px; width: 1200px; height: 617px;
    overflow: hidden;
  }
  .hero-photo {
    position: absolute; inset: 0;
    background:
      linear-gradient(90deg, #8e9a93 0%, #5f7470 28%, #4f5f45 50%, #6d5a4a 70%, #8a4a3c 85%, #a8a79e 100%);
  }
  .hero-photo::after {
    content: ""; position: absolute; inset: 0;
    background: linear-gradient(180deg, rgba(0,0,0,0) 40%, var(--hero-overlay) 100%);
  }
  .hero-content { position: absolute; left: 97px; top: 342px; color: var(--white); }
  .hero-title {
    font-size: 33px; line-height: 42px; font-weight: 400; letter-spacing: -0.3px;
  }
  .hero-lead {
    margin-top: 26px; font-size: 17px; line-height: 31px; font-weight: 300;
  }
  .help-btn {
    position: absolute; left: 1135px; top: 526px; width: 39px; height: 39px;
    border-radius: 50%; background: var(--help-bg); color: var(--white);
    font-size: 15px; display: flex; align-items: center; justify-content: center;
  }
</style>
</head>
<body>
<div class="page">
  <header class="site-header">
    <div class="brand">
      <span class="brand-dot"></span>
      <span class="brand-name">Lindqvist</span>
    </div>
    <nav class="main-nav">
      <a href="#">Coaching</a>
      <a href="#">Training</a>
      <a href="#">Ausbildung</a>
      <a href="#">Unternehmen</a>
      <a href="#">Blog</a>
      <a href="#">Kontakt</a>
    </nav>
    <div class="header-links">
      <a class="profile-link" href="#">Profil</a>
      <a class="mail-link" href="#" aria-label="E-Mail">
        <svg width="13" height="10" viewBox="0 0 13 10" fill="none" stroke="#3a3f44" stroke-width="1.4">
          <rect x="0.7" y="0.7" width="11.6" height="8.6" rx="1"/>
          <path d="M1 1.2 L6.5 5.5 L12 1.2"/>
        </svg>
      </a>
    </div>
    <a class="btn-book" href="#">Jetzt buchen</a>
  </header>

  <section class="hero">
    <div class="hero-photo" role="img" aria-label="Foto: zwei Frauen im Coaching-Gespräch auf einer Terrasse mit Pflanzen, eine hält ein Glas Wasser, die andere ein Notizbuch"></div>
    <div class="hero-content">
      <h1 class="hero-title">Ich unterstütze Sie in<br>Persönlichkeitsentwicklung<br>und Kompetenzcoaching</h1>
      <p class="hero-lead">Coaching für Privatpersonen und Teams in Firmen –<br>persönlich vor Ort oder ganz bequem von zu Hause.</p>
    </div>
    <div class="help-btn">?</div>
  </section>
</div>
</body>
</html>
```